Bussines Card Maplewood
MAPLEWOOD BARBER SHOP
Project: Bussines Card Maplewood
Bussines Card Maplewood - Salon & Spa
Creative Brief
Bright & Fun-filled
418 ELDER RD SUITE 1 ASHFORD, N.Y. 10482
maplewoodbarbershop@trimpost.net
Concepts
Business Card Design Hair Salon
Stationery Package for Nail Salon
brookhollowdeli brookhollowdeli
Phone number, fax, and info just make it bigger please.
Please only use Maplewood Barber Shop but use the same colors you've been using. Just discard the logo on the front side but on the back use the logo only. Thank you

```html
<!DOCTYPE html>
<html lang="en">
<head>
<meta charset="utf-8">
<title>Maplewood Barber Shop – Business Card</title>
<link href="https://fonts.googleapis.com/css2?family=Righteous&family=Questrial&display=swap" rel="stylesheet">
<style>
  :root {
    --page-bg: #e9e6e1;
    --brand-blue: #1f4fc4;
    --brand-blue-deep: #1840a8;
    --paper-white: #ffffff;
    --paper-shade: #e6e9f0;
    --text-light: #ffffff;
    --rule-light: rgba(255,255,255,0.85);
  }
  * { box-sizing: border-box; margin: 0; padding: 0; }
  html, body {
    width: 1200px; height: 904px; overflow: hidden;
    background: var(--page-bg);
  }
  .stage { position: relative; width: 1200px; height: 904px; }
  .card {
    position: absolute; left: 250px; width: 700px; height: 400px;
    border-radius: 22px; overflow: hidden;
    box-shadow: 0 10px 28px rgba(0,0,0,0.22);
  }
  /* Back side */
  .card-back {
    top: 32px;
    background: linear-gradient(135deg, var(--brand-blue) 0%, var(--brand-blue-deep) 100%);
    display: flex; align-items: center; justify-content: center;
  }
  .card-back .pattern-area {
    position: absolute; inset: 0;
    background: linear-gradient(135deg, rgba(255,255,255,0.04), rgba(255,255,255,0.09));
  }
  .brand-name {
    position: relative;
    font-family: "Questrial", sans-serif;
    font-size: 64px; letter-spacing: 4px;
    color: var(--text-light);
    display: flex; align-items: center; gap: 20px;
  }
  .brand-mark {
    width: 22px; height: 22px; border-radius: 50%;
    background: var(--text-light);
  }
  /* Front side */
  .card-front { top: 472px; background: var(--brand-blue); }
  .card-front .art-panel { position: absolute; inset: 0; }
  .info {
    position: absolute; left: 52px; top: 50px; width: 400px;
    color: var(--text-light);
  }
  .shop-title {
    font-family: "Righteous", sans-serif;
    font-size: 34px; line-height: 1.05; letter-spacing: 1px;
    font-weight: 400;
  }
  .dotted-rule {
    border: none; border-top: 2px dotted var(--rule-light);
    margin: 18px 0;
  }
  .address, .contacts {
    font-family: "Questrial", sans-serif;
    font-size: 20px; line-height: 1.3; letter-spacing: 0.5px;
  }
  .contacts { list-style: none; }
  .contacts li { display: flex; align-items: center; gap: 12px; }
  .contacts svg { width: 20px; height: 20px; flex: none; }
</style>
</head>
<body>
<main class="stage">

  <section class="card card-back" aria-label="Business card back">
    <div class="pattern-area" role="img" aria-label="Faint repeating scissors pattern in blue"></div>
    <div class="brand-name"><span class="brand-mark"></span>MAPLEWOOD</div>
  </section>

  <section class="card card-front" aria-label="Business card front">
    <svg class="art-panel" viewBox="0 0 700 400" preserveAspectRatio="none">
      <defs>
        <linearGradient id="paperFade" x1="0" y1="0" x2="1" y2="1">
          <stop offset="0" stop-color="var(--paper-white)"/>
          <stop offset="1" stop-color="var(--paper-shade)"/>
        </linearGradient>
      </defs>
      <polygon points="400,0 700,0 700,300 520,400 470,400"
               fill="url(#paperFade)"
               role="img" aria-label="Large open scissors illustration in blue on white"/>
    </svg>

    <div class="info">
      <h1 class="shop-title">MAPLEWOOD<br>BARBER SHOP</h1>
      <hr class="dotted-rule">
      <p class="address">418 ELDER RD<br>SUITE 4<br>ASHFORD, N.Y. 10482</p>
      <hr class="dotted-rule">
      <ul class="contacts">
        <li>
          <svg viewBox="0 0 24 24" aria-hidden="true"><path fill="#fff" d="M6.6 10.8a15 15 0 0 0 6.6 6.6l2.2-2.2a1 1 0 0 1 1-.25 11.4 11.4 0 0 0 3.6.57 1 1 0 0 1 1 1V20a1 1 0 0 1-1 1A17 17 0 0 1 3 4a1 1 0 0 1 1-1h3.5a1 1 0 0 1 1 1c0 1.25.2 2.45.57 3.6a1 1 0 0 1-.25 1z"/></svg>
          845 410 2286
        </li>
        <li>
          <svg viewBox="0 0 24 24" aria-hidden="true"><path fill="#fff" d="M6 3h12v5H6zM4 9h16a2 2 0 0 1 2 2v6h-4v4H6v-4H2v-6a2 2 0 0 1 2-2zm4 6v4h8v-4z"/></svg>
          845 410 2287
        </li>
        <li>
          <svg viewBox="0 0 24 24" aria-hidden="true"><path fill="#fff" d="M3 5h18a1 1 0 0 1 1 1v12a1 1 0 0 1-1 1H3a1 1 0 0 1-1-1V6a1 1 0 0 1 1-1zm1 2.2V17h16V7.2l-8 5.3z"/></svg>
          maplewoodbarbershop@trimpost.net
        </li>
      </ul>
    </div>
  </section>

</main>
</body>
</html>
```